Stickers to put on my honeyglasses

Stickers for my honey glasses.
Only a single sticker on the front. Same should have a stripe on the top side which goes above the lid to show if the glass was opened.
Size of the main part should be 55mm high and max. 100 mm wide.
The stripe on the top should be 70mm long.
I added a Picture of another producer which uses the same glass as I do.
I should say: 'e Lendorf Glas Hunneg'. which means 'another glass of honey. 'Hunneg' should be mainly visible and therefore very large. 'e Lendorf Glas' should be less visible and therefore smaller above the 'Hunneg'
- It needs to contain the quantity : '500gr'
- It needs to contain my Name and address: 'Marc Lendorf, 38, rue Ferd Lusang, L-9241 Miersch' (This should be small and not to visible)
- It needs to conatin a validity Line: ´Am beschte virum:` (With enough space so I can add a date by hand)
- It needs to say: 'dréchen, kill andäischterstockéieren' (to store it dry cold and dark)

```html
<!DOCTYPE html>
<html lang="lb">
<head>
<meta charset="utf-8">
<title>'e Lendorf Glas Hunneg – Etikett</title>
<link rel="stylesheet" href="https://fonts.googleapis.com/css2?family=Raleway:wght@200;300;400;600;700&display=swap">
<style>
  :root{
    --page:#ffffff;
    --kraft:#e6dccb;
    --kraft-edge:#d8ccb7;
    --cream:#f7f0e4;
    --honey:#f0b12a;
    --honey-soft:#f6d68a;
    --ink:#5a4a3a;
    --ink-soft:#8a7a66;
  }
  *{margin:0;padding:0;box-sizing:border-box}
  html,body{width:1200px;height:944px;overflow:hidden;background:var(--page)}
  body{font-family:"Raleway",sans-serif;color:var(--ink);position:relative}

  /* 70 mm seal stripe, 6.8 px per mm */
  .seal-stripe{
    position:absolute;left:516px;top:47px;width:40px;height:477px;
    background:var(--kraft);border:1px solid var(--kraft-edge);border-bottom:none;
    display:flex;align-items:flex-end;justify-content:center;padding-bottom:22px;
  }
  .seal-stripe__text{
    writing-mode:vertical-rl;transform:rotate(180deg);
    font-size:14px;font-weight:300;letter-spacing:1px;color:var(--ink);white-space:nowrap;
  }
  .seal-stripe__text strong{font-weight:400;letter-spacing:2px}

  /* 100 × 55 mm main label */
  .label{
    position:absolute;left:260px;top:523px;width:680px;height:374px;
    background:var(--kraft);border:1px solid var(--kraft-edge);
  }
  .label__head{
    display:flex;justify-content:space-between;align-items:flex-start;
    padding:14px 22px 0 22px;height:58px;
  }
  .address{font-size:10px;line-height:1.35;color:var(--ink-soft);font-weight:600;max-width:170px}
  .quantity{font-size:22px;font-weight:700;color:var(--ink);margin-top:8px}

  .label__panel{
    position:absolute;left:12px;right:12px;top:58px;bottom:12px;background:var(--cream);
    padding:12px 36px 0 36px;overflow:hidden;
  }
  .comb{position:absolute}
  .comb--left{left:0;top:0;width:120px;height:120px;
    background:radial-gradient(ellipse at 30% 40%,var(--honey-soft),rgba(247,240,228,0) 70%)}
  .comb--right{right:0;bottom:0;width:130px;height:120px;
    background:radial-gradient(ellipse at 70% 70%,var(--honey-soft),rgba(247,240,228,0) 70%)}

  .brand-line{position:relative;font-size:18px;font-weight:300;color:var(--honey);margin-left:22px;line-height:1.2}
  .product-name{
    position:relative;font-size:112px;font-weight:200;color:var(--honey);
    letter-spacing:6px;line-height:0.92;text-align:center;white-space:nowrap;
  }
  .tagline{position:relative;text-align:right;font-size:18px;font-weight:300;color:var(--honey);line-height:1.2;margin-top:2px}
  .description{position:relative;font-size:12px;line-height:1.4;color:var(--ink);margin-top:4px}
  .storage{position:relative;text-align:center;margin-top:12px;font-size:13px;line-height:1.5;font-weight:700;color:var(--ink)}
  .best-before{
    position:absolute;right:22px;bottom:10px;width:150px;height:24px;
    border-top:1px solid var(--ink-soft);font-size:9px;color:var(--ink-soft);padding-top:3px;
  }
</style>
</head>
<body>
  <div class="seal-stripe">
    <span class="seal-stripe__text">'e lendorf glas <strong>HUNNEG</strong></span>
  </div>

  <section class="label">
    <header class="label__head">
      <p class="address">Marc Lendorf, 38, rue Ferd Lusang,<br>L-9241 Miersch</p>
      <p class="quantity">500 gr</p>
    </header>

    <div class="label__panel">
      <div class="comb comb--left" role="img" aria-label="Honeycomb pattern in soft honey tones"></div>
      <div class="comb comb--right" role="img" aria-label="Honeycomb pattern in soft honey tones"></div>

      <p class="brand-line">'e lendorf glas</p>
      <h1 class="product-name">HUNNEG</h1>
      <p class="tagline">pure raw honey</p>
      <p class="description">Hunneg gëtt a klenge Quantitéiten aus lokalen Beiestäck gewonnen. Well en 100% rei an net pasteuriséiert ass, späichert en natierlech Pollen an Enzymer.</p>
      <p class="storage">'dréchen, kill andäischterstockéieren'<br>Net u Puppelcher ënner engem Joer ginn.</p>

      <p class="best-before">Am beschte virum:</p>
    </div>
  </section>
</body>
</html>
```